Brindle Financial Advice - Employer Benefit Brochure

We need to design a professional looking brochure that we can present to our existing client base, and assist in attracting new clients.
The current information is just provided in a word document, but we need to improve significantly.
The audience would be business leaders, HR decision makers and member policy committee members

Industry/Entity Type

Business

Font styles to use
Sans Serif

Colors
0255a3
f37122

```html
<!DOCTYPE html>
<html lang="en">
<head>
<meta charset="utf-8">
<title>Employer Benefits Partnership – Brindle Financial Services Group</title>
<link href="https://fonts.googleapis.com/css2?family=Archivo:ital,wght@0,700;0,800;1,800&display=swap" rel="stylesheet">
<style>
  :root {
    --brand-blue: #0255a3;
    --blue-deep: #0a3a94;
    --blue-light: #1d5fb8;
    --brand-orange: #f37122;
    --orange-light: #f79a4a;
    --white: #ffffff;
  }
  * { margin: 0; padding: 0; box-sizing: border-box; }
  html, body { width: 927px; height: 1200px; overflow: hidden; background: var(--white); }
  body { font-family: "Archivo", Arial, sans-serif; }
  .cover { position: relative; width: 927px; height: 1200px; overflow: hidden; background: var(--white); }

  .hero {
    position: absolute; left: 0; top: 0; width: 927px; height: 448px;
    background: linear-gradient(100deg, var(--blue-deep) 0%, var(--blue-light) 55%, var(--blue-deep) 100%);
  }
  .hero-title {
    position: absolute; left: 20px; top: 30px;
    color: var(--white); font-weight: 800; font-size: 90px; line-height: 128px; letter-spacing: 0.5px;
  }
  .hero-client {
    position: absolute; left: 20px; top: 318px;
    color: var(--brand-orange); font-weight: 800; font-style: italic; font-size: 74px; line-height: 90px;
  }

  .tile { position: absolute; }
  .tile-blue { background: linear-gradient(90deg, var(--blue-deep), var(--blue-light) 60%, var(--blue-deep)); }
  .tile-orange { background: linear-gradient(90deg, #ee6a1c, var(--orange-light) 55%, #ee6a1c); }
  .photo-dark { background: linear-gradient(135deg, #2a2522, #6b5d55 60%, #1b1816); }
  .photo-light { background: linear-gradient(135deg, #eef2f6, #c9d3de 60%, #e7ecf1); }
  .photo-hands { background: linear-gradient(90deg, #e9eaec, #6d6a68 45%, #2a2a2c 100%); }
  .photo-meeting { background: linear-gradient(90deg, #d9d6d2, #eef0f2 40%, #c7d4e4 70%, #dcdcdc); }

  .brand-mark {
    position: absolute; left: 30px; top: 926px; width: 158px; height: 158px;
    background: var(--brand-blue);
  }
  .brand-name {
    position: absolute; left: 210px; top: 985px;
    color: var(--brand-orange); font-weight: 700; font-size: 38px; line-height: 48px; white-space: nowrap;
  }
  .brand-address, .brand-contacts {
    position: absolute; left: 212px;
    color: var(--blue-deep); font-weight: 700; font-size: 20px; line-height: 26px; white-space: nowrap;
  }
  .brand-address { top: 1036px; }
  .brand-contacts { top: 1064px; }
  .sep { display: inline-block; width: 3px; height: 24px; background: var(--brand-orange); vertical-align: -5px; margin: 0 6px; }

  .footer-rule { position: absolute; left: 0; top: 1111px; width: 927px; height: 12px; background: var(--brand-orange); }
  .footer-band {
    position: absolute; left: 0; top: 1125px; width: 927px; height: 75px;
    background: linear-gradient(100deg, var(--blue-deep), var(--blue-light) 55%, var(--blue-deep));
  }
</style>
</head>
<body>
<main class="cover">
  <header class="hero">
    <h1 class="hero-title">Employer Benefits<br>Partnership</h1>
    <p class="hero-client">Company Name</p>
  </header>

  <section class="mosaic">
    <div class="tile photo-dark" style="left:3px;top:483px;width:191px;height:124px" role="img" aria-label="Portrait of a senior businessman in a suit"></div>
    <div class="tile tile-orange" style="left:204px;top:483px;width:179px;height:124px"></div>
    <div class="tile photo-light" style="left:392px;top:483px;width:180px;height:124px" role="img" aria-label="Young businessman looking upward"></div>
    <div class="tile photo-meeting" style="left:583px;top:483px;width:344px;height:201px" role="img" aria-label="Adviser meeting with two clients at a table"></div>
    <div class="tile tile-blue" style="left:3px;top:615px;width:191px;height:69px"></div>
    <div class="tile photo-hands" style="left:204px;top:615px;width:179px;height:69px" role="img" aria-label="Business handshake"></div>
    <div class="tile tile-blue" style="left:392px;top:615px;width:180px;height:69px"></div>
    <div class="tile tile-orange" style="left:392px;top:693px;width:180px;height:125px"></div>
    <div class="tile tile-blue" style="left:583px;top:693px;width:344px;height:125px"></div>
  </section>

  <footer class="brand">
    <div class="brand-mark"></div>
    <p class="brand-name">Brindle Financial Services Group</p>
    <p class="brand-address">14 Harbour Lane, North Sydney, 2060</p>
    <p class="brand-contacts">ph: 02 9000 4127<span class="sep"></span>www.brindlefsg.com.au<span class="sep"></span>info@brindlefsg.com.au</p>
  </footer>

  <div class="footer-rule"></div>
  <div class="footer-band"></div>
</main>
</body>
</html>
```